Corwell Holdings Business Cards

Hello. I need business cards designed with our new logo. I'd like to see at least 3 different designs. At least one with a dark background, and at least one with a white background. Maybe one with gray or blue for the background. Play with gradient colors and maybe even insert a pic of a skyline in the background of one or more of them. Use your judgement. We will need 2 cards printed. They need to accommodate the employee name, title, company address, phone, email, and website. Thanks.

Target Market(s)

Wealthy mature investors.

Contact Information for Business Card

Single-sided, professional, clean design that incorporates our logo.

Font styles to use
Sans Serif

Requirements
Must have
• Our new logo needs to be featured on it. (See attached.)
• Employee Name (In all CAPS)
• Title
• Street Address, City, ST Zip Code
• Cell Phone #, Email Address, Website Address
Nice to have
• Design that blends well with our new logo and its colors, or a city scape or other graphic design that looks like an apartment complex in the background. Blues and grays are nice, but use your judgement.
Should not have
• Modern or oriental looking designs or bright colors.

```html
<!DOCTYPE html>
<html lang="en">
<head>
<meta charset="utf-8">
<title>Corwell Holdings Business Cards</title>
<link href="https://fonts.googleapis.com/css2?family=Roboto:wght@400;500;700&family=Dancing+Script:wght@700&display=swap" rel="stylesheet">
<style>
  :root {
    --sky: #29a6df;
    --ink: #555a5f;
    --rule-grey: #8a8d90;
    --paper: #ffffff;
    --backdrop: #e6e6e4;
  }
  * { box-sizing: border-box; margin: 0; padding: 0; }
  html, body { width: 900px; height: 1200px; overflow: hidden; }
  body {
    background: var(--backdrop);
    font-family: "Roboto", Arial, sans-serif;
    position: relative;
  }
  .card {
    position: absolute;
    left: 82px;
    width: 733px;
    height: 429px;
    border-radius: 22px;
    overflow: hidden;
    box-shadow: 0 4px 10px rgba(0,0,0,.25);
  }
  .card--front { top: 138px; background: var(--paper); }
  .card--back { top: 633px; background: var(--sky); }

  .brand { position: absolute; display: flex; align-items: center; }
  .brand__mark { width: 44px; height: 44px; background: var(--sky); margin-right: 18px; }
  .brand__name { color: var(--sky); font-weight: 500; line-height: 1; text-transform: uppercase; }
  .brand__name span { display: block; }
  .brand__name .primary { font-size: 46px; letter-spacing: 1px; }
  .brand__name .secondary { font-size: 26px; margin-top: 4px; }
  .card--front .brand { left: 48px; top: 72px; }
  .card--back .brand { left: 191px; top: 178px; }
  .card--back .brand__name { color: var(--paper); }
  .card--back .brand__mark { background: var(--paper); }

  .person { position: absolute; left: 48px; top: 220px; }
  .person__name { color: var(--sky); font-size: 22px; font-weight: 700; letter-spacing: .3px; }
  .person__title { color: var(--ink); font-size: 16px; font-weight: 700; margin-top: 4px; letter-spacing: .2px; }

  .divider { position: absolute; left: 48px; top: 278px; width: 635px; height: 2px; background: var(--rule-grey); }
  .divider::before { content: ""; position: absolute; left: 0; top: 0; width: 290px; height: 2px; background: var(--sky); }

  .contact { position: absolute; left: 48px; top: 290px; list-style: none; }
  .contact li { display: flex; align-items: center; height: 26px; font-size: 16px; color: var(--ink); }
  .contact svg { width: 17px; height: 17px; margin-right: 10px; fill: var(--sky); }

  .address { position: absolute; right: 48px; top: 290px; display: flex; align-items: flex-start; }
  .address p { font-size: 16px; color: var(--ink); line-height: 26px; text-align: center; margin-right: 10px; }
  .address svg { width: 19px; height: 19px; margin-top: 3px; fill: var(--sky); }

  .tagline-band {
    position: absolute; left: 0; top: 385px; width: 100%; height: 30px;
    background: var(--sky); display: flex; align-items: center; justify-content: center;
  }
  .tagline { font-family: "Dancing Script", cursive; font-size: 20px; color: var(--paper); letter-spacing: .3px; }

  .back-web { position: absolute; left: 0; width: 100%; top: 370px; text-align: center; color: var(--paper); font-size: 16.5px; letter-spacing: .3px; }
</style>
</head>
<body>
  <section class="card card--front">
    <div class="brand">
      <div class="brand__mark"></div>
      <div class="brand__name"><span class="primary">Corwell</span><span class="secondary">Holdings, LLC</span></div>
    </div>

    <div class="person">
      <h1 class="person__name">DALE MERRICK</h1>
      <p class="person__title">INVESTOR • REAL ESTATE BROKER</p>
    </div>

    <div class="divider"></div>

    <ul class="contact">
      <li><svg viewBox="0 0 24 24"><path d="M6.6 10.8a15.1 15.1 0 0 0 6.6 6.6l2.2-2.2c.3-.3.7-.4 1-.2 1.1.4 2.3.6 3.6.6.6 0 1 .4 1 1V20c0 .6-.4 1-1 1A17 17 0 0 1 3 4c0-.6.4-1 1-1h3.5c.6 0 1 .4 1 1 0 1.3.2 2.5.6 3.6.1.3 0 .7-.2 1z"/></svg>555-014-2290</li>
      <li><svg viewBox="0 0 24 24"><path d="M2 5h20v14H2z M4 7v.5l8 5 8-5V7l-8 5z" fill-rule="evenodd"/></svg>dale@corwellholdings.com</li>
      <li><svg viewBox="0 0 24 24"><path d="M12 2a10 10 0 1 0 0 20 10 10 0 0 0 0-20zm6.9 6h-3a15 15 0 0 0-1.3-3.8A8 8 0 0 1 18.9 8zM12 4c.8 1.2 1.5 2.5 1.9 4h-3.8c.4-1.5 1.1-2.8 1.9-4zM4.3 14a8 8 0 0 1 0-4h3.4a16 16 0 0 0 0 4zm.8 2h3a15 15 0 0 0 1.3 3.8A8 8 0 0 1 5.1 16zm3-8h-3a8 8 0 0 1 4.3-3.8A15 15 0 0 0 8.1 8zM12 20c-.8-1.2-1.5-2.5-1.9-4h3.8c-.4 1.5-1.1 2.8-1.9 4zm2.3-6H9.7a14 14 0 0 1 0-4h4.6a14 14 0 0 1 0 4zm.3 5.8a15 15 0 0 0 1.3-3.8h3a8 8 0 0 1-4.3 3.8zm1.7-5.8a16 16 0 0 0 0-4h3.4a8 8 0 0 1 0 4z"/></svg>www.corwellholdings.com</li>
    </ul>

    <div class="address">
      <p>418 N. Alder, #2210<br>Brookfield, TX 75412</p>
      <svg viewBox="0 0 24 24"><path d="M12 3 2 12h3v8h5v-5h4v5h5v-8h3z"/></svg>
    </div>

    <div class="tagline-band"><p class="tagline">Building Trust. Growing Your Wealth</p></div>
  </section>

  <section class="card card--back">
    <div class="brand">
      <div class="brand__mark"></div>
      <div class="brand__name"><span class="primary">Corwell</span><span class="secondary">Holdings, LLC</span></div>
    </div>
    <p class="back-web">www.corwellholdings.com</p>
  </section>
</body>
</html>
```